QR TILL WORKS , CREDIT CARD PROCESSING EQUIPMENT

qrtillworks is a sub division of Tallow a credit car processing co.
dorian kell
14 cedar hollow ln
fernmoor 07312
suite 412

qrtillworks.example
cell 555-214-7730
office 555-861-2093
we sell pos systems to merchant who want to accept credit cards at there retail location.
black card would be nice buit open to different ideas

Target Market(s)

retail merchants

Industry/Entity Type

credit card processing

Contact Information for Business Card

card should include web site phone address

Colors

Designer to choose colors to be used in the design.

Requirements
Should not have
• red

```html
<!DOCTYPE html>
<html lang="en">
<head>
<meta charset="utf-8">
<title>QR Till Works — Business Card</title>
<link href="https://fonts.googleapis.com/css2?family=Arimo:wght@400&display=swap" rel="stylesheet">
<style>
  :root {
    --stage: #87888c;
    --card-black: #060708;
    --orange: #f6921e;
    --gold: #dccb3c;
    --white: #ffffff;
    --icon-light: #f2f3f5;
    --icon-dark: #9a9ea6;
    --icon-ink: #2a2c30;
  }
  * { margin: 0; padding: 0; box-sizing: border-box; }
  html, body {
    width: 1200px; height: 1000px; overflow: hidden;
    background: var(--stage);
    font-family: "Arimo", Arial, sans-serif;
  }
  .stage { position: relative; width: 1200px; height: 1000px; }
  .card {
    position: absolute; left: 355px; width: 570px; height: 324px;
    background: var(--card-black); border-radius: 22px; overflow: hidden;
  }
  .card--front { top: 117px; }
  .card--back { top: 477px; }
  .card__shapes { position: absolute; inset: 0; }
  .brand-mark {
    position: absolute; width: 244px; text-align: center;
    color: var(--white); font-size: 34px; line-height: 38px;
    letter-spacing: 1px; font-weight: 400;
  }
  .card--front .brand-mark { left: 284px; top: 124px; }
  .card--back .brand-mark { left: 284px; top: 137px; }
  .band-url {
    position: absolute; left: 15px; top: 146px;
    color: var(--white); font-size: 25px; line-height: 30px; font-weight: 400;
  }
  .holder-name {
    position: absolute; left: 22px; top: 29px;
    font-size: 26px; line-height: 30px; font-weight: 400; color: var(--white);
  }
  .holder-name__first { color: var(--gold); }
  .contact-row {
    position: absolute; left: 20px; display: flex; align-items: flex-start;
  }
  .contact-row__icon { width: 32px; height: 32px; flex: none; }
  .contact-row__text {
    margin-left: 12px; color: var(--white);
    font-size: 12.5px; line-height: 15.5px; font-weight: 400;
  }
  .contact-row--address { top: 86px; }
  .contact-row--address .contact-row__text { margin-top: 2px; }
  .contact-row--phone { top: 153px; }
  .contact-row--phone .contact-row__text { margin-top: 3px; }
  .contact-row--web { top: 212px; }
  .contact-row--web .contact-row__text { margin-top: 8px; }
</style>
</head>
<body>
<div class="stage">

  <section class="card card--front">
    <svg class="card__shapes" width="570" height="324" viewBox="0 0 570 324">
      <rect x="0" y="135" width="570" height="54" fill="var(--orange)"/>
      <circle cx="406" cy="162" r="134.5" fill="var(--card-black)" stroke="var(--orange)" stroke-width="25"/>
    </svg>
    <p class="band-url">qrtillworks.example</p>
    <p class="brand-mark">QR TILL<br>WORKS</p>
  </section>

  <section class="card card--back">
    <svg class="card__shapes" width="570" height="324" viewBox="0 0 570 324">
      <rect x="0" y="285" width="570" height="39" fill="var(--orange)"/>
      <circle cx="406" cy="175" r="134.5" fill="var(--card-black)" stroke="var(--orange)" stroke-width="25"/>
    </svg>

    <h1 class="holder-name"><span class="holder-name__first">DORIAN</span> KELL</h1>

    <div class="contact-row contact-row--address">
      <svg class="contact-row__icon" viewBox="0 0 32 32" aria-hidden="true">
        <defs>
          <radialGradient id="iconFill" cx="40%" cy="30%" r="75%">
            <stop offset="0" stop-color="var(--icon-light)"/>
            <stop offset="1" stop-color="var(--icon-dark)"/>
          </radialGradient>
        </defs>
        <circle cx="16" cy="16" r="15" fill="url(#iconFill)"/>
        <path d="M9 16 L16 9.5 L23 16 M11 15 V22 H21 V15" fill="none" stroke="var(--icon-ink)" stroke-width="2" stroke-linejoin="round"/>
        <rect x="14.5" y="17.5" width="3" height="4.5" fill="var(--icon-ink)"/>
      </svg>
      <p class="contact-row__text">14 cedar hollow ln<br>fernmoor 07312<br>suite 412</p>
    </div>

    <div class="contact-row contact-row--phone">
      <svg class="contact-row__icon" viewBox="0 0 32 32" aria-hidden="true">
        <circle cx="16" cy="16" r="15" fill="url(#iconFill)"/>
        <rect x="12" y="9" width="8" height="14" rx="1.5" fill="var(--icon-ink)"/>
        <rect x="13.5" y="11" width="5" height="4" fill="var(--icon-light)"/>
      </svg>
      <p class="contact-row__text">cell 555-214-7730<br>office 555-861-2093</p>
    </div>

    <div class="contact-row contact-row--web">
      <svg class="contact-row__icon" viewBox="0 0 32 32" aria-hidden="true">
        <circle cx="16" cy="16" r="15" fill="url(#iconFill)"/>
        <g fill="none" stroke="var(--icon-ink)" stroke-width="1.6">
          <circle cx="15" cy="15" r="6"/>
          <ellipse cx="15" cy="15" rx="2.5" ry="6"/>
          <path d="M9 15 H21"/>
        </g>
        <path d="M18 18 L23 20 L20.5 21 L19.5 23.5 Z" fill="var(--icon-ink)"/>
      </svg>
      <p class="contact-row__text">qrtillworks.example</p>
    </div>

    <p class="brand-mark">QR TILL<br>WORKS</p>
  </section>

</div>
</body>
</html>
```